Zielgruppe
Wir sind ein Liechtensteiner Personaldienstleisungsunternehmen welches sowohl in der klassischen Personalvermittlung als auch in der temporären Personalbereitstellung tätig ist. Unsere Branchen reichen von Baugewerbe, Handwerk, Gastro- und Hotelerie bis hin zu Produktion und Gesundheitswesen.
Achtung:
Habe gerade die files vom neuen Logo hochgeladen!!!
Aufgabenstellung
Visitienkarten designen.
Briefpapier Vorlagenerstellung.
Schlichtes Visitenkartendesign Business auf der nicht zuviele Informationen sind (das Wichtigste)
Vorderseite:
Logo (wird vor Abschluss noch in besserer Qualität hochgeladen)
Firmenname
Anschrift
Name
Funktion
Telefon
Fax
E-Mail
Homepage
Rückseite:
Kann Kreativ gestaltet werden, farblich (blau, gelb, schwarz, weiss), nach Möglichkeit keinen weissen Hintergrund.
!!Bitte keine Vorschläge mit dem Fotoscanner ... da! Danke.
Wir freuen uns auch auf kreative Vorschläge, welche etwas vom Briefing abweichen.
TKV - Team

```html
<!DOCTYPE html>
<html lang="de">
<head>
<meta charset="utf-8">
<title>TKV Personal – Geschäftsausstattung</title>
<link href="https://fonts.googleapis.com/css2?family=Arimo:wght@400;700&display=swap" rel="stylesheet">
<style>
  :root {
    --brand-blue: #1a82c4;
    --brand-blue-dark: #0b3f86;
    --brand-blue-light: #4aa9e6;
    --text-grey: #6e6e6e;
    --text-dark: #222222;
    --paper: #ffffff;
    --canvas: #ffffff;
    --shadow: rgba(0, 0, 0, 0.22);
    --sheet-edge: #d9d9d9;
  }
  * { box-sizing: border-box; margin: 0; padding: 0; }
  html, body {
    width: 1200px; height: 954px; overflow: hidden;
    background: var(--canvas);
    font-family: "Arimo", Arial, sans-serif;
    color: var(--text-grey);
  }
  .stationery { position: relative; width: 1200px; height: 954px; }

  /* ---------- business card front ---------- */
  .card {
    position: absolute; left: 56px; width: 414px; height: 268px;
    background: var(--paper);
    box-shadow: 2px 3px 6px var(--shadow);
  }
  .card--front { top: 195px; }
  .card__rule {
    position: absolute; top: 66px; height: 1px; background: var(--brand-blue-light);
  }
  .card__rule--left { left: 0; width: 124px; }
  .card__rule--right { left: 288px; right: 0; }
  .wordmark {
    color: var(--brand-blue); font-weight: 700; white-space: nowrap;
  }
  .card__wordmark {
    position: absolute; left: 124px; width: 164px; top: 40px;
    text-align: center; font-size: 26px; line-height: 52px;
  }
  .card__marker {
    position: absolute; left: 0; top: 123px; width: 16px; height: 10px;
    background: var(--brand-blue);
  }
  .card__company {
    position: absolute; left: 26px; top: 119px;
    font-size: 13px; font-weight: 700; color: var(--brand-blue);
  }
  .card__address {
    position: absolute; left: 26px; top: 137px;
    font-size: 13px; line-height: 18px;
  }
  .contact { font-size: 13px; line-height: 18.5px; border-collapse: collapse; }
  .contact td { padding: 0; white-space: nowrap; }
  .contact td:first-child { padding-right: 11px; }
  .card__contact--local { position: absolute; left: 26px; top: 183px; }
  .card__contact--abroad { position: absolute; left: 214px; top: 183px; }
  .card__contact--abroad .contact-note { font-size: 13px; line-height: 18.5px; }

  /* ---------- business card back ---------- */
  .card--back { top: 493px; overflow: hidden; }
  .card__visual {
    position: absolute; left: 0; top: 0; width: 414px; height: 238px;
    background: radial-gradient(circle at 50% 55%, #5fb4ec 0%, #1f6cc0 28%, #0d3f8e 58%, #07276a 100%);
  }
  .card__url {
    position: absolute; left: 0; right: 0; top: 241px;
    text-align: center; font-size: 15px; letter-spacing: 1px;
    color: var(--brand-blue);
  }

  /* ---------- letterhead ---------- */
  .sheet-edge {
    position: absolute; left: 1178px; top: 24px; width: 11px; height: 913px;
    background: var(--sheet-edge);
  }
  .letterhead {
    position: absolute; left: 542px; top: 20px; width: 636px; height: 917px;
    background: var(--paper);
    box-shadow: 0 0 3px rgba(0, 0, 0, 0.12);
  }
  .letterhead__wordmark {
    position: absolute; left: 440px; top: 46px; width: 150px;
    font-size: 30px; text-align: center;
  }
  .letterhead__sender {
    position: absolute; left: 72px; top: 146px;
    font-size: 7.5px; color: var(--text-dark); white-space: nowrap;
  }
  .letterhead__info { position: absolute; left: 444px; top: 142px; }
  .letterhead__company {
    font-size: 13px; font-weight: 700; color: var(--brand-blue); line-height: 16px;
  }
  .letterhead__address { font-size: 13px; line-height: 16px; margin-bottom: 14px; }
  .letterhead .contact { line-height: 16px; }
  .letterhead .contact td:first-child { padding-right: 8px; }
  .fold-mark {
    position: absolute; left: 0; width: 10px; height: 1px; background: #c8c8c8;
  }
  .fold-mark--upper { top: 325px; }
  .fold-mark--lower { top: 650px; }
  .bank {
    position: absolute; top: 862px; font-size: 10.5px; line-height: 13px;
    white-space: nowrap;
  }
  .bank--first { left: 263px; }
  .bank--second { left: 422px; }
</style>
</head>
<body>
<main class="stationery">

  <!-- Business card, front -->
  <section class="card card--front" aria-label="Visitenkarte Vorderseite">
    <div class="card__rule card__rule--left"></div>
    <div class="card__rule card__rule--right"></div>
    <div class="card__wordmark wordmark">TKV Personal</div>
    <div class="card__marker"></div>
    <div class="card__company">TKV Anstalt</div>
    <div class="card__address">Talgasse 12<br>FL-9490 Vaduz</div>
    <table class="contact card__contact--local">
      <tr><td>Telefon:</td><td>+423 555 10 20</td></tr>
      <tr><td>Telefax:</td><td>+423 555 10 21</td></tr>
      <tr><td>E-Mail:</td><td>office@tkv.li</td></tr>
    </table>
    <div class="card__contact--abroad">
      <div class="contact-note">Aus Österreich erreichbar</div>
      <table class="contact">
        <tr><td>Telefon:</td><td>+43 664 555 0142</td></tr>
        <tr><td>Telefon:</td><td>+43 664 555 03817</td></tr>
      </table>
    </div>
  </section>

  <!-- Business card, back -->
  <section class="card card--back" aria-label="Visitenkarte Rückseite">
    <div class="card__visual" role="img" aria-label="Blaue Weltkugel mit umlaufenden Pfeilen als Symbol für internationale Vermittlung"></div>
    <div class="card__url">www.tkv.li</div>
  </section>

  <!-- Letterhead -->
  <div class="sheet-edge"></div>
  <section class="letterhead" aria-label="Briefpapier">
    <div class="letterhead__wordmark wordmark">TKV Personal</div>
    <div class="letterhead__sender">TKV Anstalt · Talgasse 12 · FL-9490 Vaduz</div>
    <div class="letterhead__info">
      <div class="letterhead__company">TKV Anstalt</div>
      <div class="letterhead__address">Talgasse 12<br>FL-9490 Vaduz</div>
      <table class="contact">
        <tr><td>Telefon:</td><td>+423 555 10 20</td></tr>
        <tr><td>Telefax:</td><td>+423 555 10 21</td></tr>
        <tr><td>E-Mail:</td><td>office@tkv.li</td></tr>
        <tr><td>Internet:</td><td>www.tkv.li</td></tr>
      </table>
    </div>
    <div class="fold-mark fold-mark--upper"></div>
    <div class="fold-mark fold-mark--lower"></div>
    <div class="bank bank--first">Bregenzer Landbank<br>BLZ 30415<br>Kto.Nr. 00400008217</div>
    <div class="bank bank--second">Rheintaler Handelsbank AG<br>Kto.Nr. CHF 305.118.42<br>Kto.Nr. EUR 305.224.61</div>
  </section>

</main>
</body>
</html>
```